Graphic for Customer Journey for Apartment Renter

We need to update our Customer Journey Graphic. Below is the current graphic and a list of updates.
We are a property management company that owns and manages 55 apartment communities across the Southeast US. As part of our employee training, we define the customer experience, the touch-points within and what we expect at each stage. Currently we have 5 stages within the Calloway Experience “cycle”: Leasing, New Resident, Resident, Renewal and Move Out. We’re looking to define the Resident Experience a little more. It may mean that visually, the straight line becomes a line with a loop. Once the resident enters the resident experience, they’ll definitely interact with us to Pay Rent and most likely to Submit a Work Order. There are a number of additional touch point opportunities. At the end of the resident cycle, they either renew their contract with us and re-enter the resident cycle or they move out. I’ve added a rough visual of this below as well.
We’re looking for someone with journey mapping experience to use their creative license to update the graphic of our customer journey map in consideration for the above.
The current customer journey map, The Calloway Experience - in attached file

Rough Visual of more defined Resident Experience - in attached file

Straight line journey becomes a journey with a loop? Not married to this. Just an idea. - in attached file

Target Market(s)

employees

Industry/Entity Type

Property Management

Logo Text

defined within description - see supporting doc as well

Colors
85cae6

Requirements
Must have
• defined within
Nice to have
• defined within
Should not have
• defined within

```html
<!DOCTYPE html>
<html lang="en">
<head>
<meta charset="utf-8">
<title>Resident Journey Key</title>
<link rel="stylesheet" href="https://fonts.googleapis.com/css2?family=Oswald:wght@500;600&display=swap">
<style>
  :root {
    --bg-light: #f4f4f4;
    --bg-dark: #b9b9b9;
    --stage-dark: #5f5f5f;
    --stage-blue: #1f5aa6;
    --stage-grey: #9c9c9c;
    --renewal-blue: #7b9dd4;
    --hub: #d6d6d6;
    --ink: #ffffff;
  }
  html, body {
    margin: 0;
    padding: 0;
    overflow: hidden;
  }
  .journey-canvas {
    width: 1200px;
    height: 717px;
    overflow: hidden;
    background: radial-gradient(ellipse 70% 75% at 42% 48%, var(--bg-light) 0%, #dcdcdc 55%, var(--bg-dark) 100%);
  }
  .journey-map {
    display: block;
    width: 1200px;
    height: 717px;
  }
  .stage-label,
  .ring-label,
  .touchpoint-label {
    font-family: "Oswald", "Arial Narrow", sans-serif;
    fill: var(--ink);
    text-transform: uppercase;
  }
  .stage-label { font-size: 14px; font-weight: 600; letter-spacing: 0.4px; }
  .stage-label--large { font-size: 18px; }
  .ring-label { font-size: 20px; font-weight: 600; letter-spacing: 1.2px; }
  .touchpoint-label { font-size: 11.5px; font-weight: 600; letter-spacing: 0.3px; }
  .stage-leasing { fill: var(--stage-dark); }
  .stage-new-resident { fill: var(--stage-blue); }
  .stage-move-out { fill: var(--stage-grey); }
  .ring-resident { fill: var(--stage-dark); }
  .ring-renewal { fill: var(--renewal-blue); }
  .touchpoint-disc { fill: var(--stage-blue); }
  .key-hub { fill: var(--hub); }
  .icon { fill: var(--ink); }
  .icon-line { fill: none; stroke: var(--ink); stroke-width: 2; stroke-linecap: round; stroke-linejoin: round; }
  .icon-line--blue { fill: none; stroke: var(--stage-blue); stroke-width: 1.4; stroke-linecap: round; }
  .disc-divider { stroke: #2d66b2; stroke-width: 1; }
</style>
</head>
<body>
<div class="journey-canvas">
  <svg class="journey-map" viewBox="0 0 900 538" xmlns="http://www.w3.org/2000/svg" aria-label="Resident journey shown as a key">
    <defs>
      <path id="resident-arc" d="M568,140 A152,152 0 0 1 798,317"/>
      <path id="renewal-arc" d="M536,384 A168,168 0 0 0 820,294"/>
    </defs>

    <!-- Key shaft: move out stage with teeth -->
    <path class="stage-move-out" d="M30,248 L470,248 L470,325 L345,325 L327,292 L305,325 L268,325 L248,292 L228,325 L192,325 L172,292 L152,325 L132,325 L114,292 L48,292 Z"/>

    <!-- Key shaft: leasing and new resident stages -->
    <polygon class="stage-leasing" points="80,188 285,188 300,209 285,230 80,230 62,209"/>
    <polygon class="stage-new-resident" points="285,188 500,188 500,230 285,230 300,209"/>

    <!-- Renewal pointer joining the shaft -->
    <polygon class="ring-renewal" points="472,222 445,266 472,310 560,310 560,222"/>

    <!-- Key bow: renewal and resident rings -->
    <circle class="ring-renewal" cx="655" cy="265" r="178"/>
    <path class="ring-resident" d="M491,195 A178,178 0 0 1 830,296 L781,287 A128,128 0 0 0 537,215 Z"/>
    <circle class="touchpoint-disc" cx="655" cy="265" r="128"/>
    <line class="disc-divider" x1="598" y1="210" x2="560" y2="170"/>
    <line class="disc-divider" x1="712" y1="265" x2="783" y2="265"/>
    <line class="disc-divider" x1="598" y1="320" x2="560" y2="360"/>
    <circle class="key-hub" cx="655" cy="265" r="57"/>

    <!-- Leasing stage -->
    <g class="icon-handshake" transform="translate(108,198)">
      <path class="icon" d="M0,6 L9,2 L18,6 L26,2 L36,6 L36,14 L28,22 L22,24 L14,18 L8,18 L0,14 Z"/>
      <path class="icon-line--blue" d="M12,8 L18,12 M16,10 L24,16 M20,12 L27,18"/>
    </g>
    <text class="stage-label" x="203" y="206" text-anchor="middle">Leasing</text>
    <text class="stage-label" x="203" y="224" text-anchor="middle">Experience</text>

    <!-- New resident stage -->
    <g class="icon-key" transform="translate(312,196)">
      <rect class="icon" x="8" y="0" width="16" height="14" rx="3"/>
      <circle class="icon" cx="7" cy="18" r="6"/>
      <path class="icon-line" d="M7,22 L3,32 M4,28 L8,29"/>
    </g>
    <text class="stage-label" x="402" y="206" text-anchor="middle">New Resident</text>
    <text class="stage-label" x="402" y="224" text-anchor="middle">Experience</text>

    <!-- Move out stage -->
    <text class="stage-label stage-label--large" x="120" y="274">Move Out Experience</text>
    <g class="icon-truck" transform="translate(365,266)">
      <rect class="icon" x="12" y="0" width="46" height="28"/>
      <path class="icon" d="M0,14 L4,6 L11,6 L11,28 L0,28 Z"/>
      <circle class="icon" cx="8" cy="32" r="5"/>
      <circle class="icon" cx="36" cy="32" r="5"/>
      <circle class="icon" cx="49" cy="32" r="5"/>
    </g>

    <!-- Ring titles -->
    <g class="icon-bed" transform="translate(516,146) rotate(-28)">
      <path class="icon-line" d="M0,0 L0,20 M0,14 L36,14 L36,20 M4,8 L34,8 L34,14"/>
      <circle class="icon" cx="8" cy="8" r="3"/>
    </g>
    <text class="ring-label"><textPath href="#resident-arc">The Resident Experience</textPath></text>

    <g class="icon-form" transform="translate(526,352) rotate(30)">
      <rect class="icon-line" x="0" y="0" width="18" height="22" rx="1"/>
      <path class="icon-line" d="M4,6 L14,6 M4,11 L14,11 M4,16 L9,16 M13,20 L21,6"/>
    </g>
    <text class="ring-label"><textPath href="#renewal-arc" startOffset="40">The Renewal Exience</textPath></text>

    <!-- Touchpoints -->
    <g class="icon-coins" transform="translate(638,148)">
      <ellipse class="icon" cx="17" cy="26" rx="16" ry="5"/>
      <ellipse class="icon" cx="17" cy="20" rx="16" ry="5"/>
      <circle class="icon" cx="17" cy="10" r="11"/>
      <text x="17" y="15" text-anchor="middle" font-family="Oswald, sans-serif" font-size="13" font-weight="600" fill="#1f5aa6">$</text>
    </g>
    <text class="touchpoint-label" x="655" y="200" text-anchor="middle">Paying Rent</text>

    <g class="icon-renewal-form" transform="translate(550,232)">
      <rect class="icon-line" x="0" y="0" width="18" height="24" rx="1"/>
      <path class="icon-line" d="M4,7 L14,7 M4,12 L14,12 M4,17 L9,17 M13,21 L22,6"/>
    </g>
    <text class="touchpoint-label" x="563" y="276" text-anchor="middle">Renewal</text>
    <text class="touchpoint-label" x="563" y="292" text-anchor="middle">Exience</text>

    <g class="icon-work-order" transform="translate(642,322)">
      <path class="icon-line" d="M0,0 L16,0 L24,8 L24,34 L0,34 Z M16,0 L16,8 L24,8"/>
    </g>
    <text class="touchpoint-label" x="654" y="372" text-anchor="middle">Submit Work</text>
    <text class="touchpoint-label" x="654" y="387" text-anchor="middle">Order</text>
  </svg>
</div>
</body>
</html>
```